Project VOIP Phone

Lumerix Antilles needs a advertisement design for a new product called a VOIP PHONE. A VOIP Phone stands for Voice Over Internet Protocol. The advantages in comparison with a PSTN (Packet-Switched Telephone Network) are that a VOIP system saves a lot of money. Besides that it is simple, flexible and is the future of telecom.
The text of the advertisement should be:
' Get your VOIP PHONE SYSTEM starting at ƒ 25,- per phone (p/m)'
'VOIP PHONE SYSTEM' and 'ƒ 25,-' should be bigger than the rest, '(p/m)' should be smaller than the rest.
Under that our contact data should follow:
Lumerix Antilles
Tel: +599 9 732-1184
E-mail: sales@lumerix-demo.cw
Website: www.lumerix-demo.cw
The last rule of the Banner must contain a small text:
''Lumerix Cloud Solotions & Management''
We want to receive an optional design with some watermarks in the back with 2 or 3 words like: "cheap'' ''solid'' or ''reliable'' ''up coming'' ''Future'' or something like that.
We also want some pictures (attached) in the banner. Not al the pictures are needed, just whatever looks best on it.
The banner must have a size of: 728x200.
Good luck!
Updates
Please help us with this interesting project in the future of telephony

```html
<!DOCTYPE html>
<html lang="en">
<head>
<meta charset="utf-8">
<title>Lumerix Antilles – VOIP Phone System banners</title>
<link rel="stylesheet" href="https://fonts.googleapis.com/css2?family=Ubuntu:wght@400;500;700&display=swap">
<style>
  :root{
    --stage:#e9e6e1;
    --white:#ffffff;
    --ink:#111111;
    --blue-deep:#0a5fb8;
    --blue-mid:#1a8ae6;
    --blue-light:#5cc0ff;
    --strip:#0b3f78;
    --yellow:#ffd21a;
    --btn-top:#ffe14a;
    --btn-bottom:#f7ad00;
    --btn-text:#4a2e00;
    --brand:#1b3f8c;
    --cloud-a:#cfeeff;
    --cloud-b:#7fc8f0;
    --watermark:rgba(0,55,120,.5);
  }
  *{margin:0;padding:0;box-sizing:border-box}
  html,body{width:1200px;height:787px;overflow:hidden}
  body{background:var(--stage);font-family:"Ubuntu",sans-serif;position:relative}

  .banner{position:absolute;left:95px;width:1012px;height:276px;background:var(--white);
    box-shadow:0 4px 14px rgba(0,0,0,.18);overflow:hidden}
  .banner--plain{top:86px}
  .banner--watermark{top:423px}

  .banner__panel{position:absolute;inset:0}
  .banner__art{position:absolute;left:55px;top:28px;width:215px;height:200px;border-radius:50%;
    background:radial-gradient(circle at 50% 45%,var(--cloud-a) 0%,var(--cloud-b) 55%,rgba(127,200,240,0) 72%)}

  .watermark{position:absolute;z-index:2;font-weight:700;color:var(--watermark);
    letter-spacing:2px;font-size:19px;line-height:20px;white-space:nowrap}
  .watermark--affordable{left:2px;top:75px;transform:rotate(-62deg)}
  .watermark--reliable{left:210px;top:182px;transform:rotate(-45deg)}

  .headline{position:absolute;inset:0;color:var(--white);line-height:1;font-weight:700;white-space:nowrap}
  .headline span{position:absolute}
  .headline__lead{font-size:30px;text-shadow:0 2px 3px rgba(0,0,0,.35)}
  .headline__product{color:var(--yellow);font-size:44px;text-shadow:0 2px 3px rgba(0,0,0,.35)}
  .headline__system{color:var(--yellow);font-size:66px;text-shadow:0 2px 3px rgba(0,0,0,.35)}
  .headline__from{font-size:21px;font-weight:500}
  .headline__price{color:var(--yellow);font-size:58px;text-shadow:0 2px 3px rgba(0,0,0,.35)}
  .headline__unit{font-size:21px;font-weight:500}
  .headline__period{font-size:18px;font-weight:500}

  .contact{position:absolute;left:30px;top:250px;width:690px;display:flex;gap:30px;
    color:var(--white);font-size:15.5px;white-space:nowrap}
  .contact b{font-weight:700}

  .brand{position:absolute;left:770px;top:26px;width:230px;text-align:center}
  .brand__mark{width:86px;height:86px;margin:0 auto 18px;border:7px solid var(--ink);border-radius:12px;background:var(--blue-light)}
  .brand__name{font-size:30px;font-weight:700;color:var(--brand);line-height:1}

  .cta{position:absolute;left:773px;top:199px;width:215px;height:42px;border-radius:21px;
    background:linear-gradient(var(--btn-top),var(--btn-bottom));box-shadow:0 2px 3px rgba(0,0,0,.3);
    color:var(--btn-text);font-size:21px;font-weight:500;display:flex;align-items:center;
    padding-left:18px}
  .cta__arrow{position:absolute;right:10px;top:10px;width:22px;height:22px}

  .tagline{position:absolute;right:6px;top:257px;text-align:right;
    font-size:10.5px;font-weight:700;color:var(--ink);white-space:nowrap}
</style>
</head>
<body>

<section class="banner banner--plain" aria-label="VOIP phone system banner">
  <svg class="banner__panel" viewBox="0 0 1012 276" width="1012" height="276" aria-hidden="true">
    <defs>
      <radialGradient id="rays1" cx="38%" cy="45%" r="65%">
        <stop offset="0" stop-color="#5cc0ff"/>
        <stop offset=".55" stop-color="#1a8ae6"/>
        <stop offset="1" stop-color="#0a5fb8"/>
      </radialGradient>
    </defs>
    <path d="M24 0 Q-4 138 24 276 L752 276 Q786 138 752 0 Z" fill="#111111"/>
    <path d="M30 0 Q8 138 30 276 L728 276 Q758 138 728 0 Z" fill="url(#rays1)"/>
    <rect x="20" y="244" width="720" height="32" fill="#0b3f78"/>
  </svg>
  <div class="banner__art" role="img" aria-label="Cloud with telephone handset circled by two arrows"></div>

  <div class="headline">
    <span class="headline__lead" style="left:285px;top:10px">Get your</span>
    <span class="headline__product" style="left:285px;top:42px">VOIP PHONE</span>
    <span class="headline__system" style="left:368px;top:88px">SYSTEM</span>
    <span class="headline__from" style="left:285px;top:168px">starting at</span>
    <span class="headline__price" style="left:405px;top:160px">ƒ 25,-</span>
    <span class="headline__unit" style="left:580px;top:166px">per phone</span>
    <span class="headline__period" style="left:634px;top:192px">(p/m)</span>
  </div>

  <div class="contact">
    <span>Tel: <b>+599 9 732-1184</b></span>
    <span>E-mail: <b>sales@lumerix-demo.cw</b></span>
    <span>Website: <b>www.lumerix-demo.cw</b></span>
  </div>

  <div class="brand">
    <div class="brand__mark" aria-hidden="true"></div>
    <div class="brand__name">Lumerix</div>
  </div>
  <div class="cta">Find Out More
    <svg class="cta__arrow" viewBox="0 0 22 22" aria-hidden="true"><path d="M8 5l6 6-6 6" fill="none" stroke="#4a2e00" stroke-width="3" stroke-linecap="round" stroke-linejoin="round"/></svg>
  </div>
  <p class="tagline">Lumerix Cloud Solotions and Managed Services</p>
</section>

<section class="banner banner--watermark" aria-label="VOIP phone system banner with watermark words">
  <svg class="banner__panel" viewBox="0 0 1012 276" width="1012" height="276" aria-hidden="true">
    <defs>
      <radialGradient id="rays2" cx="40%" cy="45%" r="65%">
        <stop offset="0" stop-color="#5cc0ff"/>
        <stop offset=".55" stop-color="#1a8ae6"/>
        <stop offset="1" stop-color="#0a5fb8"/>
      </radialGradient>
    </defs>
    <path d="M24 0 Q-4 138 24 276 L752 276 Q786 138 752 0 Z" fill="#111111"/>
    <path d="M30 0 Q8 138 30 276 L728 276 Q758 138 728 0 Z" fill="url(#rays2)"/>
    <rect x="20" y="244" width="720" height="32" fill="#0b3f78"/>
  </svg>
  <div class="banner__art" role="img" aria-label="Cloud with telephone handset circled by two arrows"></div>
  <span class="watermark watermark--affordable">AFFORDABLE</span>
  <span class="watermark watermark--reliable">RELIABLE</span>

  <div class="headline">
    <span class="headline__lead" style="left:310px;top:10px">Get your</span>
    <span class="headline__product" style="left:310px;top:42px">VOIP PHONE</span>
    <span class="headline__system" style="left:392px;top:88px">SYSTEM</span>
    <span class="headline__from" style="left:310px;top:168px">starting at</span>
    <span class="headline__price" style="left:430px;top:160px">ƒ 25,-</span>
    <span class="headline__unit" style="left:605px;top:166px">per phone</span>
    <span class="headline__period" style="left:659px;top:192px">(p/m)</span>
  </div>

  <div class="contact">
    <span>Tel: <b>+599 9 732-1184</b></span>
    <span>E-mail: <b>sales@lumerix-demo.cw</b></span>
    <span>Website: <b>www.lumerix-demo.cw</b></span>
  </div>

  <div class="brand">
    <div class="brand__mark" aria-hidden="true"></div>
    <div class="brand__name">Lumerix</div>
  </div>
  <div class="cta">Find Out More
    <svg class="cta__arrow" viewBox="0 0 22 22" aria-hidden="true"><path d="M8 5l6 6-6 6" fill="none" stroke="#4a2e00" stroke-width="3" stroke-linecap="round" stroke-linejoin="round"/></svg>
  </div>
  <p class="tagline">Lumerix Cloud Solotions and Managed Services</p>
</section>

</body>
</html>
```